The Copper Ladder

we require a classy business card design for a business coaching company that uses our current logo and the wording:

Front of card:

LOGO
Kyle Morrison
CEO
TEL: 1300 4 52918
FAX: 1300 5 52918
Mobile: 0412 638194
PO Box 917, Ferris Hollow, Brisbane, Qld 4127
e: kylem@copperladder.com.au
w: www.copperladder.com.au

Reverse side of the card:

Systematizing Businesses into Turnkey Operations
Strategic Business Plans
Sales & Marketing Programs
Sales Training & Business Coaching
Internet Marketing & Web Design

Here’s what our clients say:

“We grew from $396,000 to over $5million in 4 years and made KTS’s Rising Enterprises Roll 3 years running!” – Martin Greaves, Meridian Works

Target Market(s)

small to medium sized business owners in Australia

Industry/Entity Type

Business

Requirements
Must have
• standard business card size

```html
<!DOCTYPE html>
<html lang="en">
<head>
<meta charset="utf-8">
<title>The Copper Ladder – Business Card</title>
<link rel="stylesheet" href="https://fonts.googleapis.com/css2?family=Open+Sans:wght@400;700;800&display=swap">
<style>
  :root {
    --page: #ffffff;
    --ink: #111111;
    --ink-soft: #2a2a2a;
    --grey-light: #f2f2f2;
    --grey-mid: #c9c9c9;
    --grey-dark: #9a9a9a;
    --yellow-bright: #fff35c;
    --yellow-deep: #f6c800;
    --swoosh: #ffffff;
  }
  * { margin: 0; padding: 0; box-sizing: border-box; }
  html, body {
    width: 970px; height: 1200px; overflow: hidden;
    background: var(--page);
  }
  .canvas { position: relative; width: 970px; height: 1200px; }
  .card {
    position: absolute; left: 105px; width: 759px;
    overflow: hidden; color: var(--ink);
    font-family: "Open Sans", Verdana, sans-serif;
  }
  .card-front {
    top: 74px; height: 380px;
    background: linear-gradient(160deg, var(--grey-light) 0%, var(--grey-mid) 55%, var(--grey-dark) 100%);
  }
  .card-back {
    top: 600px; height: 422px;
    background: radial-gradient(ellipse at 45% 20%, #ffffff 0%, var(--grey-light) 45%, var(--grey-mid) 100%);
  }
  .front-swoosh { position: absolute; inset: 0; }

  .brand-name {
    position: absolute;
    font-family: "Open Sans", Verdana, sans-serif;
    font-weight: 700; color: var(--ink);
    line-height: 1; white-space: nowrap;
  }
  .card-front .brand-name { right: 40px; top: 74px; font-size: 36px; }
  .card-back .brand-name { left: 470px; top: 218px; font-size: 28px; }

  .contact { position: absolute; left: 22px; top: 168px; }
  .contact-name { font-size: 24px; font-weight: 800; line-height: 28px; }
  .contact-title { font-size: 17px; font-weight: 700; line-height: 23px; }
  .contact-line { font-size: 17px; font-weight: 400; line-height: 23px; white-space: nowrap; }

  .services { position: absolute; left: 26px; top: 22px; list-style: none; }
  .service {
    font-size: 21px; font-weight: 700; line-height: 28px;
    margin-bottom: 28px; white-space: nowrap;
  }
  .testimonial { position: absolute; left: 26px; top: 326px; right: 22px; }
  .testimonial-heading { font-size: 19px; font-weight: 700; margin-bottom: 8px; }
  .testimonial-quote { font-size: 14px; font-weight: 700; line-height: 23px; }
</style>
</head>
<body>
<main class="canvas">

  <section class="card card-front" aria-label="Card front">
    <svg class="front-swoosh" width="759" height="380" viewBox="0 0 759 380" aria-hidden="true">
      <defs>
        <radialGradient id="yellowGlow" cx="70%" cy="20%" r="75%">
          <stop offset="0%" stop-color="#fffbd0"/>
          <stop offset="30%" stop-color="#fff35c"/>
          <stop offset="100%" stop-color="#f6c800"/>
        </radialGradient>
      </defs>
      <path d="M140 0 C 250 180, 500 260, 759 255 L 759 0 Z" fill="var(--swoosh)"/>
      <path d="M235 0 C 320 130, 520 200, 759 195 L 759 0 Z" fill="url(#yellowGlow)"/>
    </svg>

    <p class="brand-name">The Copper Ladder</p>

    <div class="contact">
      <p class="contact-name">Kyle Morrison</p>
      <p class="contact-title">CEO</p>
      <p class="contact-line">TEL: 1300 4 52918</p>
      <p class="contact-line">FAX: 1300 5 52918</p>
      <p class="contact-line">Mobile: 0412 638194</p>
      <p class="contact-line">PO Box 917, Ferris Hollow, Brisbane, Qld 4127</p>
      <p class="contact-line">e: kylem@copperladder.com.au</p>
      <p class="contact-line">w: www.copperladder.com.au</p>
    </div>
  </section>

  <section class="card card-back" aria-label="Card back">
    <ul class="services">
      <li class="service">• Systematizing Businesses into Turnkey Operations •</li>
      <li class="service">• Sales Training &amp; Business Coaching •</li>
      <li class="service">• Internet Marketing &amp; Web Design •</li>
      <li class="service">• Sales &amp; Marketing Programs •</li>
      <li class="service">• Strategic Business Plans •</li>
    </ul>

    <p class="brand-name">The Copper Ladder</p>

    <div class="testimonial">
      <p class="testimonial-heading">Here’s what our clients say:</p>
      <blockquote class="testimonial-quote">“We grew from $396,000 to over $5million in 4 years and made KTS’s Rising Enterprises Roll 3 years running!” – Martin Greaves, Meridian Works</blockquote>
    </div>
  </section>

</main>
</body>
</html>
```